New Brand - Website Design (4 Pages)

We are launching a new brand for electronic cigarettes. We already have logo and packaging done and would like a web design to go with it.

We are interested in the following deliverables:

1) Home Page Design
2) Check Out Design
3) How it Works Page
4) Secondary Template Page Design

Looking for a 60s modern look and something that is consistent with our logo and packaging.

Industry/Entity Type

Electronic

Requirements
Must have
• Consistent with logo and packaging (Use Logo Attached)
White background

Example (Functionality & Design): http://www.brolvap.co.uk/
Example (Design): http://www.plumtorva.com/

We want the design more like plumtorva but the functionality the same as brolvap.

Top Bar: Pella Marks Kits; Cartridge Refills; How it Works; Contact; My Account; Checkout
Should not have
• Stock List or Search Bar or Newsletter Signup

```html
<!DOCTYPE html>
<html lang="en">
<head>
<meta charset="utf-8">
<title>Pella Marks — Home</title>
<link rel="stylesheet" href="https://fonts.googleapis.com/css2?family=Oswald:wght@300;400;500&family=PT+Serif:wght@400;700&display=swap">
<style>
  :root {
    --ink: #1a1a1a;
    --black: #000;
    --white: #fff;
    --panel: #2e2e2e;
    --panel-light: #444;
    --rule: #333;
    --muted: #555;
    --gold-top: #e2cd3a;
    --gold-bottom: #a88c12;
    --gold-text: #d6b92a;
    --footer: #161616;
    --footer-text: #cfcfcf;
    --video-blue: #1a9be0;
    --head: "Oswald", sans-serif;
    --body: "PT Serif", serif;
  }
  * { box-sizing: border-box; margin: 0; padding: 0; }
  html, body { width: 806px; height: 1200px; overflow: hidden; background: var(--white); }
  body { position: relative; font-family: var(--body); color: var(--ink); }

  .top-strip { position: absolute; left: 0; top: 0; width: 806px; height: 6px; background: var(--black); }

  .brand { position: absolute; top: 44px; left: 0; width: 806px; text-align: center; }
  .brand-name { font-family: var(--head); font-weight: 500; font-size: 34px; color: var(--black); letter-spacing: 1px; white-space: nowrap; }

  .main-nav { position: absolute; left: 54px; top: 106px; width: 700px; height: 30px; background: var(--black); display: flex; align-items: center; padding-left: 81px; gap: 26px; }
  .main-nav a { color: var(--white); text-decoration: none; font-family: var(--body); font-size: 11.5px; letter-spacing: 0.6px; position: relative; white-space: nowrap; }
  .main-nav a.active::after { content: ""; position: absolute; left: 50%; bottom: -13px; margin-left: -6px; border: 6px solid transparent; border-top-color: var(--black); border-bottom: 0; }

  .hero { position: absolute; left: 54px; top: 136px; width: 700px; height: 254px; display: flex; }
  .hero-offer { width: 246px; height: 100%; background: radial-gradient(ellipse at 50% 40%, var(--panel-light), var(--panel) 75%); text-align: center; color: var(--white); padding-top: 22px; }
  .hero-offer h2 { font-family: var(--head); font-weight: 400; font-size: 20px; letter-spacing: 0.3px; text-transform: uppercase; border-bottom: 2px solid #bbb; display: inline-block; padding-bottom: 2px; white-space: nowrap; }
  .hero-offer h2 em { font-style: normal; color: var(--gold-text); }
  .hero-offer .kit { font-family: var(--head); font-weight: 300; font-size: 18px; margin-top: 4px; }
  .price-ring { width: 102px; height: 102px; margin: 10px auto 0; border-radius: 50%; border: 1px dashed #999; display: flex; align-items: center; justify-content: center; }
  .price-ring span { width: 88px; height: 88px; border-radius: 50%; border: 1px dashed #777; display: flex; align-items: center; justify-content: center; font-family: var(--head); font-weight: 300; font-size: 30px; color: #ddd; }
  .buy-btn { display: inline-block; margin-top: 14px; width: 96px; height: 30px; line-height: 30px; border-radius: 3px; background: linear-gradient(var(--gold-top), var(--gold-bottom)); color: var(--ink); font-family: var(--head); font-weight: 300; font-size: 17px; text-decoration: none; }
  .hero-photo { flex: 1; background: linear-gradient(100deg, #d9d9d9 0%, #9a9a9a 45%, #4a4a4a 70%, #8a8a8a 100%); }

  .section-title { position: absolute; left: 53px; width: 701px; display: flex; align-items: center; gap: 12px; }
  .section-title::before, .section-title::after { content: ""; height: 3px; background: var(--rule); flex: 1; }
  .section-title h3 { font-family: var(--head); font-weight: 400; font-size: 19px; font-variant: small-caps; color: var(--rule); letter-spacing: 0.5px; white-space: nowrap; }
  .title-kits { top: 388px; }
  .title-kits::before { flex: 0 0 299px; }
  .title-why { top: 560px; }
  .title-why::before { flex: 0 0 299px; }
  .title-community { top: 846px; }
  .title-community::before { flex: 0 0 278px; }

  .kit-grid { position: absolute; left: 54px; top: 424px; display: flex; gap: 9px; }
  .kit-card { position: relative; width: 168px; height: 126px; border: 1px dotted #ccc; padding: 6px; }
  .kit-card .kit-photo { width: 100%; height: 100%; background: radial-gradient(ellipse at 50% 50%, #3a3a3a 0%, #1c1c1c 45%, #fff 72%); }
  .kit-card .kit-label { position: absolute; left: 0; bottom: 0; width: 100%; height: 49px; background: rgba(60,60,60,0.85); color: var(--white); font-size: 13px; letter-spacing: 0.6px; display: flex; align-items: center; justify-content: center; white-space: nowrap; }

  .video { position: absolute; left: 54px; top: 592px; width: 444px; height: 248px; border: 1px solid #ddd; background: linear-gradient(110deg, #f0f0f0 0%, #bdbdbd 40%, #3a3a3a 70%, #d0d0d0 100%); }
  .video-actions { position: absolute; right: 9px; top: 9px; display: flex; flex-direction: column; gap: 5px; }
  .video-actions span { width: 36px; height: 27px; border-radius: 4px; background: #3a4a4a; color: var(--white); font-family: var(--head); font-size: 6.5px; display: flex; flex-direction: column; align-items: center; justify-content: flex-end; padding-bottom: 3px; gap: 2px; }
  .video-actions svg { width: 12px; height: 12px; }
  .play-btn { position: absolute; left: 8px; bottom: 9px; width: 52px; height: 31px; border-radius: 3px; background: #3a4a4a; display: flex; align-items: center; justify-content: center; }
  .scrub { position: absolute; left: 68px; bottom: 9px; width: 367px; height: 26px; border-radius: 3px; background: #3a4a4a; display: flex; align-items: center; padding: 0 8px; gap: 8px; }
  .scrub .track { width: 270px; height: 9px; border: 1px solid #aaa; background: linear-gradient(90deg, var(--video-blue) 0 28%, #777 28% 79%, #333 79%); }
  .scrub .hd { font-family: var(--head); font-weight: 500; font-style: italic; font-size: 11px; color: var(--video-blue); }

  .why-copy { position: absolute; left: 506px; top: 590px; width: 250px; font-size: 10.5px; line-height: 17px; letter-spacing: 0.6px; }
  .why-copy p { font-weight: 700; color: var(--ink); }
  .why-copy ul { list-style: none; margin-top: 10px; font-size: 10px; color: var(--muted); }
  .why-copy li { line-height: 22.5px; white-space: nowrap; }
  .why-copy li::before { content: "➤"; margin-right: 8px; color: var(--ink); font-size: 9px; }

  .community { position: absolute; left: 0; top: 890px; width: 806px; display: flex; justify-content: center; gap: 29px; }
  .community a { display: flex; flex-direction: column; align-items: center; gap: 8px; width: 70px; text-decoration: none; color: var(--rule); font-family: var(--head); font-size: 18px; font-variant: small-caps; }
  .community a::before { content: ""; width: 66px; height: 66px; border-radius: 50%; background: var(--rule); }

  .site-footer { position: absolute; left: 0; top: 1010px; width: 806px; height: 190px; background: var(--footer); color: var(--footer-text); }
  .about-title { position: absolute; left: 72px; top: 12px; width: 682px; display: flex; align-items: center; gap: 10px; }
  .about-title h4 { font-family: var(--head); font-weight: 400; font-size: 19px; font-variant: small-caps; color: #ddd; white-space: nowrap; }
  .about-title::after { content: ""; flex: 1; height: 2px; background: #3a3a3a; }
  .footer-brand { position: absolute; left: 70px; top: 44px; width: 126px; height: 98px; border: 3px solid #2a2a2a; background: var(--black); display: flex; align-items: center; justify-content: center; }
  .footer-brand b { font-family: var(--head); font-weight: 500; font-size: 17px; color: var(--white); white-space: nowrap; letter-spacing: 0.5px; }
  .about-copy { position: absolute; left: 214px; top: 52px; width: 210px; font-size: 8.5px; line-height: 17px; letter-spacing: 0.5px; }
  .footer-col { position: absolute; top: 32px; font-size: 8.5px; letter-spacing: 0.8px; }
  .footer-col h5 { font-size: 10px; font-weight: 700; color: #e8e8e8; margin-bottom: 4px; letter-spacing: 0.4px; white-space: nowrap; }
  .footer-col li { list-style: none; line-height: 17.2px; white-space: nowrap; }
  .col-products { left: 463px; }
  .col-ordering { left: 590px; }
  .copyright { position: absolute; left: 0; bottom: 8px; width: 806px; text-align: center; font-size: 9px; letter-spacing: 0.8px; }
</style>
</head>
<body>
  <div class="top-strip"></div>

  <header class="brand">
    <span class="brand-name">PELLA MARKS</span>
  </header>

  <nav class="main-nav">
    <a class="active" href="#">Pella Marks Kits</a>
    <a href="#">Cartridge Refills</a>
    <a href="#">How it Works</a>
    <a href="#">Contact</a>
    <a href="#">My Account</a>
    <a href="#">Checkout</a>
  </nav>

  <section class="hero">
    <div class="hero-offer">
      <h2>Pella Marks <em>Best</em> Seller</h2>
      <div class="kit">pella marks starter kit</div>
      <div class="price-ring"><span>$12.00</span></div>
      <a class="buy-btn" href="#">Buy now</a>
    </div>
    <div class="hero-photo" role="img" aria-label="Black and white photo of a man holding an electronic cigarette in his mouth by the sea"></div>
  </section>

  <div class="section-title title-kits"><h3>Pella Marks Kits</h3></div>
  <section class="kit-grid">
    <div class="kit-card">
      <div class="kit-photo" role="img" aria-label="Starter kit box with cartridges and charger"></div>
      <div class="kit-label">Kit name goes here</div>
    </div>
    <div class="kit-card"><div class="kit-photo" role="img" aria-label="Starter kit box with cartridges and charger"></div></div>
    <div class="kit-card"><div class="kit-photo" role="img" aria-label="Starter kit box with cartridges and charger"></div></div>
    <div class="kit-card"><div class="kit-photo" role="img" aria-label="Starter kit box with cartridges and charger"></div></div>
  </section>

  <div class="section-title title-why"><h3>Why Pella Marks?</h3></div>
  <section class="video" role="img" aria-label="Video still of a man in a dark coat using an electronic cigarette">
    <div class="video-actions">
      <span><svg viewBox="0 0 12 12"><path d="M6 11 1 6a2.6 2.6 0 0 1 5-3 2.6 2.6 0 0 1 5 3z" fill="#fff"/></svg>LIKE</span>
      <span><svg viewBox="0 0 12 12"><circle cx="6" cy="6" r="5" fill="none" stroke="#fff" stroke-width="1.4"/><path d="M6 3v3l2 1.5" stroke="#fff" stroke-width="1.3" fill="none"/></svg>LATER</span>
      <span><svg viewBox="0 0 12 12"><circle cx="3" cy="6" r="1.6" fill="#fff"/><circle cx="9" cy="2.5" r="1.6" fill="#fff"/><circle cx="9" cy="9.5" r="1.6" fill="#fff"/><path d="M3 6 9 2.5M3 6l6 3.5" stroke="#fff"/></svg>SHARE</span>
      <span><svg viewBox="0 0 12 12"><path d="M4 3 1 6l3 3M8 3l3 3-3 3M7 2 5 10" stroke="#fff" stroke-width="1.3" fill="none"/></svg>EMBED</span>
    </div>
    <div class="play-btn"><svg width="14" height="14" viewBox="0 0 14 14"><path d="M2 1l11 6-11 6z" fill="#fff"/></svg></div>
    <div class="scrub"><div class="track"></div><span class="hd">HD</span></div>
  </section>
  <div class="why-copy">
    <p>Lorem ipsum dolor sit amet, consectetur adipiscing elit. Aenean hendrerit ac sem et ullamcorper. Mauris in dui eget eros fermentum dignissim non eu leo. Vivamus id magna hendrerit, tincidunt nulla nec, porttitor augue.</p>
    <ul>
      <li>Lorem ipsum dolor sit amet, consectetur adip.</li>
      <li>30% ipsum dolor sit amet, consectetur adip.</li>
      <li>Lorem ipsum dolor sit amet, consectetur adip.</li>
      <li>Edolor sit amet, consectetur adip.</li>
      <li>Ipsum dolor imet, consectetur adip.</li>
    </ul>
  </div>

  <div class="section-title title-community"><h3>Pella Marks Community</h3></div>
  <nav class="community">
    <a href="#">Chirpline</a>
    <a href="#">Friendpage</a>
    <a href="#">Workmesh</a>
  </nav>

  <footer class="site-footer">
    <div class="about-title"><h4>About Pella Marks</h4></div>
    <div class="footer-brand"><b>PELLA MARKS</b></div>
    <p class="about-copy">Lorem ipsum dolor sit amet, consectetur adipiscing elit. Aenean hendrerit ac sem et ullamcorper. Mauris in dui eget eros fermentum dignissim non eu leo. Vivamus id magna hendrerit, tincidunt nulla nec, porttitor augue.</p>
    <div class="footer-col col-products">
      <h5>Pella Marks Products</h5>
      <ul><li>Product 1</li><li>Product 2</li><li>Product 3</li><li>Product 4</li><li>Product 5</li></ul>
    </div>
    <div class="footer-col col-ordering">
      <h5>Ordering Information</h5>
      <ul><li>Returns Policy</li><li>Ordering Information</li><li>Warranty</li><li>Customer Service</li><li>FAQs</li></ul>
    </div>
    <div class="copyright">Copyright 2013 Pella Marks - Terms &amp; Conditions | Privacy Policy</div>
  </footer>
</body>
</html>
```